Independent IT Consulting Professional. Looking for a clean crisp, somewhat traditional design. I have also attached the initial off-the-shelf design from PrintHaven. My company has grown quickly, and I would like to take the card to the next level. Should be sharp, mature, classy well laid-out and convey confidence. I don't think the off-the-shelf design does this. I like the logo I have for the time being, but if someone has something better in mind, I would be happy to consider an alternative. I would also like to see the color Cyan used in a small way, either with the logo or some other color treatment, as I feel like this is a modern color that I always liked, but never was able to make anything work with it.
Industry/Entity Type
It Company
Contact Information for Business Card
Carter J. Whitlow
Owner
TrellMark Solutions
2817 Ashborough Lane
Corwin Falls, NY 12990
(555) 555-0148
cwhitlow@trellmarksolutions.example
www.trellmarksolutions.example
Tagline: Business Technology Services and Consulting

```html
<!DOCTYPE html>
<html lang="en">
<head>
<meta charset="utf-8">
<title>TrellMark Solutions – Business Card</title>
<link href="https://fonts.googleapis.com/css2?family=Lato:ital,wght@0,400;0,700;0,900;1,400&display=swap" rel="stylesheet">
<style>
  :root {
    --backdrop: #6a6a6a;
    --card-white: #ffffff;
    --brand-blue: #2a5caa;
    --brand-blue-deep: #234f96;
    --ink: #1d1d1f;
    --swoosh-black: #111111;
    --accent-cyan: #1fb6e0;
    --text-light: #ffffff;
  }
  * { margin: 0; padding: 0; box-sizing: border-box; }
  html, body {
    width: 1200px;
    height: 900px;
    overflow: hidden;
    background: var(--backdrop);
    font-family: "Lato", Arial, sans-serif;
  }
  .card {
    position: absolute;
    left: 75px;
    top: 150px;
    width: 1050px;
    height: 600px;
    background: var(--card-white);
    overflow: hidden;
    box-shadow: 0 12px 30px rgba(0,0,0,0.35);
  }
  .card-waves {
    position: absolute;
    inset: 0;
    width: 100%;
    height: 100%;
  }
  .brand {
    position: absolute;
    right: 60px;
    top: 70px;
    display: flex;
    align-items: center;
    gap: 12px;
  }
  .brand-dot {
    width: 22px;
    height: 22px;
    border-radius: 50%;
    background: var(--accent-cyan);
  }
  .brand-name {
    font-weight: 900;
    font-size: 34px;
    color: var(--brand-blue-deep);
    line-height: 1;
  }
  .person {
    position: absolute;
    right: 60px;
    top: 250px;
    text-align: right;
  }
  .person-name {
    font-size: 40px;
    color: var(--ink);
    font-weight: 400;
    line-height: 1.1;
  }
  .person-name strong { font-weight: 700; }
  .person-title {
    font-size: 20px;
    color: var(--brand-blue);
    letter-spacing: 3px;
    margin-top: 2px;
  }
  .contact {
    position: absolute;
    left: 50px;
    top: 235px;
    color: var(--text-light);
  }
  .company {
    font-size: 30px;
    font-weight: 700;
    margin-bottom: 4px;
  }
  .address {
    font-size: 23px;
    line-height: 1.35;
    margin-bottom: 18px;
  }
  .lines {
    list-style: none;
    font-size: 22px;
    line-height: 1.35;
  }
  .lines b { font-weight: 900; margin-right: 6px; }
  .tagline {
    position: absolute;
    left: 50px;
    bottom: 30px;
    color: var(--text-light);
    font-size: 22px;
    font-weight: 700;
    letter-spacing: 5px;
    text-transform: uppercase;
  }
  .tagline em {
    text-transform: none;
    font-weight: 400;
    letter-spacing: 2px;
  }
</style>
</head>
<body>
  <main class="card">
    <svg class="card-waves" viewBox="0 0 1050 600" preserveAspectRatio="none" aria-hidden="true">
      <path d="M0,128 C220,92 360,110 470,240 C570,360 760,450 1050,425" fill="none" stroke="var(--brand-blue)" stroke-width="7"/>
      <path d="M600,390 C760,450 920,430 1050,370 L1050,455 C900,480 740,470 600,390 Z" fill="var(--swoosh-black)"/>
      <path d="M0,150 C210,118 340,132 440,250 C540,370 740,470 1050,462 L1050,600 L0,600 Z" fill="var(--brand-blue)"/>
    </svg>

    <div class="brand">
      <span class="brand-dot"></span>
      <span class="brand-name">TrellMark Solutions</span>
    </div>

    <div class="person">
      <p class="person-name">Carter J. <strong>Whitlow</strong></p>
      <p class="person-title">OWNER</p>
    </div>

    <div class="contact">
      <p class="company">TrellMark Solutions</p>
      <p class="address">2817 Ashborough Lane, Corwin Falls,<br>NY 12990</p>
      <ul class="lines">
        <li><b>P.</b>(555) 555-0148</li>
        <li><b>W.</b>www.trellmarksolutions.example</li>
        <li><b>E.</b>cwhitlow@trellmarksolutions.example</li>
      </ul>
    </div>

    <p class="tagline">Business Technology Services <em>and</em> Consulting</p>
  </main>
</body>
</html>
```